illustration of the importance of using your money as voting power for the environment

Illustration to read either per word, or creative interpretation (open to suggestions) " Vote, use your $ to vote for your favourite candidate" and then below it will have two choices the first reading "Berries- imported (yes), regulated (questionable), Free trade over Free Health (absolutely)" second choice reading "Berries- local (yes), organic (hopefully), regulated (most definatley) Free trade over Free Health (not on Australia's watch). there will be a little thought bubble next to the second choice that says "I know we cost more, but do you think people will get it yet?). It must have my logo on the bottom. I have uploaded the file.

The project is about using your money or your wallet to make a choice, making that choice is equal to voting. Every time you buy something, you are voting for a 'good' project, one that is environmentally friendly and gives positvely to the environment OR you are voting/buying a 'bad' product that is unsustainable, potentially poisonous and damages people and the environment. We just had a health scare here becuase of imported berries that were not regulated because of our new free trade agreement with china, although this is not about china, its about be aware as a consumer and making or Voting for your future.

Target Market(s)

20's- 50's

Industry/Entity Type

Environment

Requirements
Must have
• my logo and business name

```html
<!DOCTYPE html>
<html lang="en">
<head>
<meta charset="utf-8">
<title>Vote With Your Dollar – Berries</title>
<link rel="stylesheet" href="https://fonts.googleapis.com/css2?family=Source+Sans+3:wght@400;600;700&display=swap">
<style>
  :root {
    --board-green: #1a5538;
    --map-green: #2a6a47;
    --ribbon-red: #ef4d4f;
    --ribbon-shade: #c93a3d;
    --label-gold: #f5b335;
    --note-beige: #cfc6ad;
    --chart-beige: #c7bca3;
    --bubble-white: #ffffff;
    --bubble-edge: #d9d9d9;
    --brand-green: #87ad3a;
    --brand-ink: #1f1f1f;
    --hand-yellow: #f2bf2a;
    --note-green: #3c8a4a;
  }
  * { margin: 0; padding: 0; box-sizing: border-box; }
  html, body { width: 1200px; height: 1002px; overflow: hidden; background: var(--board-green); }
  .canvas {
    position: relative; width: 1200px; height: 1002px; overflow: hidden;
    background: var(--board-green);
    font-family: "Source Sans 3", "Myriad Pro", Arial, sans-serif;
  }
  .world-map {
    position: absolute; left: 165px; top: 390px; width: 840px; height: 280px;
    border-radius: 120px;
    background: radial-gradient(ellipse at center, rgba(60,125,85,.55), rgba(42,106,71,.15) 70%, transparent);
  }
  .artwork { position: absolute; left: 0; top: 0; }
  .label { position: absolute; white-space: nowrap; line-height: 1; }
  .label--gold { color: var(--label-gold); }
  .label--beige { color: var(--note-beige); }
  .choice-answer--absolutely { left: 242px; top: 218px; font-size: 27px; }
  .choice-answer--not { left: 780px; top: 210px; width: 140px; text-align: center; font-size: 20px; line-height: 28px; white-space: normal; }
  .free-trade { left: 445px; top: 228px; font-size: 19px; }
  .organic-no { left: 380px; top: 335px; font-size: 26px; }
  .organic-axis { left: 487px; top: 340px; font-size: 21px; }
  .organic-hopefully { left: 658px; top: 333px; font-size: 29px; }
  .regulated-questionable { left: 224px; top: 467px; font-size: 28px; }
  .regulated-definitely { left: 763px; top: 467px; font-size: 28px; }
  .berries-imported { left: 238px; top: 558px; font-size: 28px; }
  .berries-local { left: 697px; top: 558px; font-size: 28px; }
  .brand-name {
    position: absolute; left: 560px; top: 100px; font-size: 40px; font-weight: 600;
    color: var(--brand-ink);
  }
  .brand-dot {
    position: absolute; left: 600px; top: 42px; width: 52px; height: 52px;
    border-radius: 50%; background: var(--brand-green);
  }
  .thought-text {
    position: absolute; left: 934px; top: 74px; width: 200px;
    font-size: 17px; font-weight: 700; line-height: 21px; color: var(--brand-green);
  }
  .hand-with-note {
    position: absolute; left: 470px; top: 865px; width: 180px; height: 100px;
    border-radius: 40px 50px 30px 30px;
    background: linear-gradient(160deg, var(--hand-yellow) 0 45%, var(--note-green) 45%);
  }
</style>
</head>
<body>
<main class="canvas">
  <div class="world-map" role="img" aria-label="Faint world map in the background"></div>

  <svg class="artwork" width="1200" height="1002" viewBox="0 0 1200 1002">
    <!-- speech bubbles -->
    <g class="brand-bubble">
      <path d="M770,150 C720,190 560,200 520,140 C480,80 560,25 650,30 C740,35 790,80 775,130 L808,165 Z" fill="var(--bubble-white)" stroke="var(--bubble-edge)" stroke-width="2"/>
    </g>
    <g class="thought-bubble">
      <path d="M900,160 C940,200 1140,200 1160,120 C1175,60 1110,30 1030,35 C950,40 905,80 915,125 L868,168 Z" fill="var(--bubble-white)" stroke="var(--bubble-edge)" stroke-width="2"/>
    </g>

    <!-- choice ribbons -->
    <g class="choice-ribbon" fill="none" stroke="var(--ribbon-red)" stroke-width="55">
      <path d="M330,290 C330,360 335,420 420,425 C505,430 525,460 525,520 L525,582"/>
      <path d="M830,290 C830,360 825,420 740,425 C650,430 618,460 618,520 L618,582"/>
    </g>
    <circle class="choice-head" cx="308" cy="218" r="107" fill="var(--ribbon-red)"/>
    <circle class="choice-head" cx="850" cy="218" r="108" fill="var(--ribbon-red)"/>

    <!-- vote arrows -->
    <g class="vote-arrow" transform="translate(470,665) rotate(-40)">
      <rect x="-14" y="-10" width="28" height="50" fill="var(--ribbon-shade)"/>
      <polygon points="-28,-8 0,-42 28,-8" fill="var(--ribbon-red)"/>
    </g>
    <g class="vote-arrow" transform="translate(700,665) rotate(40)">
      <rect x="-14" y="-10" width="28" height="50" fill="var(--ribbon-shade)"/>
      <polygon points="-28,-8 0,-42 28,-8" fill="var(--ribbon-red)"/>
    </g>

    <!-- growth chart -->
    <g class="growth-chart" fill="var(--chart-beige)">
      <rect x="512" y="800" width="18" height="16" rx="4"/>
      <rect x="538" y="785" width="18" height="31" rx="4"/>
      <rect x="564" y="762" width="18" height="54" rx="4"/>
      <rect x="590" y="735" width="22" height="81" rx="4"/>
      <path d="M514,768 C545,740 580,712 605,690" fill="none" stroke="var(--chart-beige)" stroke-width="9" stroke-linecap="round"/>
      <polygon points="594,680 620,676 612,702"/>
    </g>
  </svg>

  <span class="brand-dot"></span>
  <span class="brand-name">spendWell</span>
  <p class="thought-text">I know we cost more, but do you think people will get it yet?</p>

  <span class="label label--gold choice-answer--absolutely">Absolutely</span>
  <span class="label label--beige free-trade">Free trade over Free Health</span>
  <span class="label label--gold choice-answer--not">Not on Australia's watch</span>

  <span class="label label--beige organic-no">NO</span>
  <span class="label label--beige organic-axis">&lt;=organic=&gt;</span>
  <span class="label label--beige organic-hopefully">Hopefully</span>

  <span class="label label--beige regulated-questionable">Questionable</span>
  <span class="label label--beige regulated-definitely">Most definatley</span>

  <span class="label label--gold berries-imported">Berries - imported</span>
  <span class="label label--gold berries-local">Berries- local</span>

  <div class="hand-with-note" role="img" aria-label="Hand holding out a banknote"></div>
</main>
</body>
</html>
```